Harbinger and Lantern Website

We are a private investigation that people turn to when they seek answers. We provide all types of investigation services as well as security and debt collection but mainly we specialise in digital forensic investigation. This site will be the first representation that potential clients see. We need a site that can work on all browsers so not too many animations. The theme we are going for is "Pallor" the TV show but keeping the law enforcement look. We want it to expand on the logo of our company that is strength and pride (refer to files attached). The logo and mission statement must stand out.
The relevant info is attached in .doc documents
Updates

Hi,

I have uploaded a slightly different version of the logo and I do prefer the new version and made a FEW but important updates and additions to the website info. Sorry for the inconvenience.

Hi, 

Sorry just one last thing can you please put the following on the website 'Harbinger and Lantern is a South Australian owned business and we service all of Australia.' 

I have increased the budget.

Hi,

I've increased the budget slightly. I will continue to increase it as long as the quality of designs match it.

I have increased the budget. I will increase it more if I see some designs that warrant the increase.

I have extended the deadline by 3 days.

Hi,

Forget the brief and please take a look at this link and that is the type of design I want. I want people to look at it and think modern, professional, digital, forensic investigation. I have not seen anything that makes me think "wow" so please submit some new designs. I will increase the budget when I start to see designs that I like. 

regarding the last message, this is the link

https://www.vantorel-example.org

Reason: Have not seen anything that stands out from the rest.

Reason: To let designers finish off their current concepts that they may be working on.

Target Market(s)

Average to corporate people seeking professionalism and a firm that can supply answers that traditional law enforcement agencies fail to provide

Industry/Entity Type

Security

Requirements
Must have
• A professional QRD, Southern Tablelands Constabulary website look mixed with a theme from the TV show "Pallor" and the ability to download the business cards (refer to attached files)
Should not have
• cartoon images and anything relating to Ambrose Pettigrew

```html
<!DOCTYPE html>
<html lang="en">
<head>
<meta charset="utf-8">
<title>Harbinger and Lantern</title>
<link href="https://fonts.googleapis.com/css2?family=PT+Sans:wght@400;700&display=swap" rel="stylesheet">
<style>
:root{
  --header-light:#f6f3ea;
  --header-warm:#e7e2d4;
  --black:#000;
  --panel:#1b1b1b;
  --panel-dark:#141414;
  --rule:#4a4a4a;
  --text-soft:#bdbdbd;
  --text-muted:#8c8c8c;
  --heading:#c9c9c9;
  --hero-text:#5d5d5d;
  --hero-strong:#8e8e8e;
  --gold-top:#e6dcae;
  --gold-bottom:#b8a670;
  --footer:#a9a9a9;
  --white:#fff;
}
*{box-sizing:border-box;margin:0;padding:0}
html,body{width:1200px;height:1050px;overflow:hidden}
body{font-family:"PT Sans",Arial,sans-serif;background:var(--black);position:relative}
.site{position:relative;width:1200px;height:1050px}

.topbar{position:absolute;left:0;top:0;width:1200px;height:96px;
  background:radial-gradient(ellipse at 55% 30%,var(--header-light),var(--header-warm))}
.brand{position:absolute;left:136px;top:38px;display:flex;align-items:center;gap:10px;
  font-size:19px;font-weight:700;color:#3a3528}
.brand-dot{width:22px;height:22px;border-radius:50%;background:#3a3528}
.contact{position:absolute;left:855px;top:9px;color:#333}
.contact dt{font-size:19px;font-weight:700;line-height:22px}
.contact dd{font-size:14px;color:#666;line-height:18px;margin-bottom:8px}
.contact a{color:#666}

.nav{position:absolute;left:417px;top:96px;display:flex;height:37px}
.nav a{display:block;color:var(--white);text-decoration:none;font-size:18px;line-height:40px;padding:0 23px;letter-spacing:.2px}
.nav a.is-active{background:var(--white);color:#333}

.hero{position:absolute;left:0;top:133px;width:1200px;height:430px;background:var(--black)}
.hero-photo{position:absolute;left:690px;top:0;width:510px;height:430px;
  background:radial-gradient(ellipse at 42% 55%,#4a4a4a 0%,#262626 35%,#0d0d0d 75%)}
.hero-lede{position:absolute;left:126px;top:114px;width:440px;font-size:29px;line-height:38px;color:var(--hero-text)}
.hero-lede strong{color:var(--hero-strong)}
.btn-gold{position:absolute;left:127px;top:251px;width:214px;height:45px;
  background:linear-gradient(var(--gold-top),var(--gold-bottom));border-radius:2px;
  color:#2a2718;font-size:20px;line-height:45px;text-align:center;text-decoration:none}

.content{position:absolute;left:0;top:563px;width:1200px;height:438px;
  background:linear-gradient(var(--panel),var(--panel-dark))}
.gallery-title{position:absolute;left:127px;top:24px;font-size:19px;color:var(--heading);letter-spacing:.3px}
.gallery-arrow{position:absolute;top:84px}
.gallery-arrow.prev{left:131px}
.gallery-arrow.next{left:1051px}
.thumb{position:absolute;top:62px;width:164px;height:88px}
.t1{left:166px;background:linear-gradient(120deg,#0d1420,#3c4a5c 60%,#1a1a1a)}
.t2{left:343px;background:linear-gradient(90deg,#111,#2b2b2b 50%,#8a7a55)}
.t3{left:518px;background:linear-gradient(100deg,#1e1a1a,#6b5f5f 55%,#3d3535)}
.t4{left:694px;background:linear-gradient(#c6a287,#7a5845 60%,#1a1e2a)}
.t5{left:870px;background:linear-gradient(110deg,#6f8fbf,#24304a 60%,#0c1020)}

.col{position:absolute;top:192px}
.col h2{font-size:23px;font-weight:400;font-variant:small-caps;color:var(--heading);
  padding-bottom:4px;border-bottom:1px solid var(--rule);padding-left:2px}
.col p,.col li{font-size:13px;line-height:20px;color:var(--text-soft)}
.col-cases{left:123px;width:268px}
.col-cases p{margin-top:25px;width:290px}
.col-why{left:503px;width:268px}
.col-why ul{list-style:none;margin-top:25px}
.col-why a{color:var(--text-muted)}
.col-services{left:851px;width:238px}
.col-services h2{padding-left:11px}
.col-services ul{list-style:none;margin-top:25px;padding-left:9px}
.col-services li{display:flex;align-items:center;gap:7px}
.read-more{display:block;margin-top:5px;font-size:11px;color:var(--text-muted)}
.col-cases .read-more{margin-left:-2px}
.col-services .read-more{margin-left:22px;margin-top:6px}

.footer{position:absolute;left:0;top:1001px;width:1200px;height:49px;background:var(--footer);
  text-align:center;color:var(--white);font-size:12px}
.footer-links{padding-top:7px;line-height:16px}
.footer-links a{color:var(--white);text-decoration:none;margin:0 6px}
.footer small{display:block;font-size:12px;margin-top:3px}
</style>
</head>
<body>
<div class="site">
  <header class="topbar">
    <div class="brand"><span class="brand-dot"></span>Harbinger and Lantern</div>
    <dl class="contact">
      <dt>Call:</dt><dd>(0400) 555-017</dd>
      <dt>Email:</dt><dd><a href="#">managers@harbingerlantern.example</a></dd>
    </dl>
  </header>

  <section class="hero">
    <div class="hero-photo" role="img" aria-label="Uniformed security officer holding a torch in the dark"></div>
    <p class="hero-lede"><strong>Harbinger and Lantern</strong> is a South Australian owned business and we service all of Australia.</p>
    <a class="btn-gold" href="#">Learn more About Us</a>
  </section>

  <nav class="nav">
    <a class="is-active" href="#">HOME</a>
    <a href="#">ABOUT</a>
    <a href="#">PRODUCTS</a>
    <a href="#">SERVICES</a>
    <a href="#">CAREERS</a>
    <a href="#">CONTACT</a>
  </nav>

  <main class="content">
    <h2 class="gallery-title">OUR SERVICE GALLERY</h2>
    <svg class="gallery-arrow prev" width="24" height="44" viewBox="0 0 24 44"><polyline points="22,1 2,22 22,43" fill="none" stroke="#ddd" stroke-width="1.5"/></svg>
    <div class="thumb t1" role="img" aria-label="Magnifying glass over a laptop keyboard"></div>
    <div class="thumb t2" role="img" aria-label="Masked intruder at a doorway"></div>
    <div class="thumb t3" role="img" aria-label="Gloved hand picking a door lock"></div>
    <div class="thumb t4" role="img" aria-label="Close-up of watchful eyes"></div>
    <div class="thumb t5" role="img" aria-label="Masked figure at a computer"></div>
    <svg class="gallery-arrow next" width="24" height="44" viewBox="0 0 24 44"><polyline points="2,1 22,22 2,43" fill="none" stroke="#ddd" stroke-width="1.5"/></svg>

    <section class="col col-cases">
      <h2>Unsolved cases</h2>
      <p>Lorem Ipsum is simply dummy text of the print-ing and typesetting industry. Lorem Ipsum has been the industry's standard dummy text ever since the 1500s, when an unknown printer took a galley of type and scrambled it to make a type specimen book. It has survived not only five</p>
      <a class="read-more" href="#">Read More</a>
    </section>

    <section class="col col-why">
      <h2>Why Choose Us</h2>
      <ul>
        <li><a href="#">Lorem Ipsum is simply</a> dummy text of the</li>
        <li>Lorem Ipsum is simply</li>
        <li>Lorem Ipsum is</li>
        <li><a href="#">Lorem Ipsum is simply</a> dummy</li>
        <li><a href="#">Lorem Ipsum is simply</a> dummy text of the</li>
        <li><a href="#">Lorem Ipsum is simply</a> dummy text of the</li>
      </ul>
      <a class="read-more" href="#">Read More</a>
    </section>

    <section class="col col-services">
      <h2>Services</h2>
      <ul>
        <li><svg width="7" height="9" viewBox="0 0 7 9"><polyline points="1,1 5,4.5 1,8" fill="none" stroke="#fff" stroke-width="2"/></svg>Unsolved Cases</li>
        <li><svg width="7" height="9" viewBox="0 0 7 9"><polyline points="1,1 5,4.5 1,8" fill="none" stroke="#fff" stroke-width="2"/></svg>Bullying/Stalking</li>
        <li><svg width="7" height="9" viewBox="0 0 7 9"><polyline points="1,1 5,4.5 1,8" fill="none" stroke="#fff" stroke-width="2"/></svg>Missing Persons</li>
        <li><svg width="7" height="9" viewBox="0 0 7 9"><polyline points="1,1 5,4.5 1,8" fill="none" stroke="#fff" stroke-width="2"/></svg>Child recovery</li>
        <li><svg width="7" height="9" viewBox="0 0 7 9"><polyline points="1,1 5,4.5 1,8" fill="none" stroke="#fff" stroke-width="2"/></svg>Con Men and Con Women</li>
        <li><svg width="7" height="9" viewBox="0 0 7 9"><polyline points="1,1 5,4.5 1,8" fill="none" stroke="#fff" stroke-width="2"/></svg>Pre-marital checks</li>
      </ul>
      <a class="read-more" href="#">Read More</a>
    </section>
  </main>

  <footer class="footer">
    <div class="footer-links">
      <a href="#">Home</a>|<a href="#">About</a> |<a href="#">Product</a>|<a href="#">Services</a>|<a href="#">Career</a>
    </div>
    <small>©2012 Harbinger Lantern, Inc</small>
  </footer>
</div>
</body>
</html>
```